Flyerdesign for a Sports Homepage

I need a design for our Merchandise/Discount Flyer.
we are going to sell high class sports equipment.
the flyer should be in Size A5 or between A5 and A4.
there should be mentioned our Product names:
Product name for powerlifting: Torvik
Product name for Boxing: ZL Boxing
Product name for Martial Arts: Murelt
Product name for MMA: PitVolt
Product name for Bodybuilding: Bramfold

our Storename: PushAndDuel
Homepage: www.pushandduel.example

there should be space for entering a discount code
shop logo and brand logos: all pictures are attached.

out of the box thinking is welcome

Target Market(s)

People who do powersports like powerlifting or mma

Industry/Entity Type

Sport

Requirements
Must have
• 2 sides, all our brandnames, homepage, shop name and sports

```html
<!DOCTYPE html>
<html lang="en">
<head>
<meta charset="utf-8">
<title>PushAndDuel – Discount Flyer</title>
<link rel="stylesheet" href="https://fonts.googleapis.com/css2?family=Montserrat:wght@600;700;800&family=Open+Sans:wght@300&display=swap">
<style>
  :root {
    --ink: #231f20;
    --gold: #c9ac6d;
    --gold-pale: #d6c488;
    --brand-blue: #1a55a5;
    --cyan: #15a9cc;
    --white: #ffffff;
    --paper: #ffffff;
    --caption: #1a1a1a;
    --badge-yellow: #f2c31c;
  }
  * { margin: 0; padding: 0; box-sizing: border-box; }
  html, body { width: 1200px; height: 900px; overflow: hidden; background: var(--paper); }
  .canvas { position: relative; width: 1200px; height: 900px; font-family: "Montserrat", sans-serif; }
  .artwork { position: absolute; inset: 0; }

  .shop-mark {
    position: absolute; display: flex; align-items: center; justify-content: center;
    border: 2px solid var(--gold); background: #1e1e1e;
    color: var(--gold); font-weight: 700; font-size: 12px; letter-spacing: 1.5px;
  }
  .shop-mark--front { left: 62px; top: 73px; width: 147px; height: 99px; }
  .shop-mark--back { left: 990px; top: 72px; width: 146px; height: 98px; }

  .shop-name {
    position: absolute; left: 60px; top: 188px;
    color: var(--gold-pale); font-weight: 800; font-size: 20px; letter-spacing: 0.2px;
  }

  .product-card {
    position: absolute; left: 48px; top: 268px; width: 431px; height: 404px;
    background: var(--white); border: 1.5px solid var(--brand-blue);
  }
  .product-card__title {
    position: absolute; left: 60px; top: 278px;
    color: var(--brand-blue); font-weight: 800; font-size: 43px; letter-spacing: -0.5px; white-space: nowrap;
  }

  .product-row { position: absolute; left: 16px; width: 548px; height: 49px; }
  .product-row__sport {
    position: absolute; left: 0; top: 0; width: 280px; height: 49px;
    border-radius: 25px 0 0 25px;
    background: linear-gradient(90deg, var(--cyan) 0%, #8fdcec 55%, #ffffff 100%);
    padding-left: 44px; line-height: 49px;
    color: var(--ink); font-weight: 800; font-size: 27px; letter-spacing: -1.2px; white-space: nowrap;
  }
  .product-row__name {
    position: absolute; left: 256px; top: 0; width: 292px; height: 49px;
    background: var(--ink); border: 1.5px solid var(--white); border-radius: 25px;
    padding-left: 32px; line-height: 46px;
    color: var(--white); font-weight: 800; font-size: 31px; white-space: nowrap;
  }

  .brand-logos__label {
    position: absolute; left: 153px; top: 712px;
    color: var(--gold); font-weight: 800; font-size: 14px; letter-spacing: 0.3px;
  }
  .brand-logos { position: absolute; left: 46px; top: 744px; display: flex; gap: 8px; }
  .brand-logos__slot { width: 50px; height: 50px; background: var(--white); }

  .discount {
    position: absolute; left: 700px; top: 601px; width: 152px; height: 152px;
    display: flex; flex-direction: column; align-items: center; justify-content: center;
    color: var(--ink); font-weight: 800; line-height: 0.9;
  }
  .discount__value { font-size: 60px; letter-spacing: -2px; }
  .discount__label { font-size: 24px; }

  .website {
    position: absolute; left: 598px; width: 358px; top: 778px; text-align: center;
    color: var(--white); font-weight: 800; font-size: 19px;
  }

  .caption {
    position: absolute; top: 846px; font-family: "Open Sans", sans-serif; font-weight: 300;
    font-size: 26px; color: var(--caption);
  }
  .caption--front { left: 245px; }
  .caption--back { left: 857px; }
</style>
</head>
<body>
<main class="canvas">
  <svg class="artwork" viewBox="0 0 1200 900" width="1200" height="900">
    <defs>
      <linearGradient id="stripeBlue" x1="0" y1="0" x2="1" y2="1">
        <stop offset="0" stop-color="#0a7cc4"/>
        <stop offset="1" stop-color="#1a3a5a" stop-opacity="0"/>
      </linearGradient>
      <linearGradient id="stripeTeal" x1="0" y1="0" x2="1" y2="1">
        <stop offset="0" stop-color="#2bc0c0"/>
        <stop offset="1" stop-color="#0a6aa8" stop-opacity="0"/>
      </linearGradient>
      <linearGradient id="cornerBlue" x1="0" y1="0" x2="1" y2="1">
        <stop offset="0" stop-color="#1d5f8a"/>
        <stop offset="0.4" stop-color="#0a84d0"/>
        <stop offset="1" stop-color="#0078c8"/>
      </linearGradient>
      <linearGradient id="cornerGold" x1="0" y1="0" x2="1" y2="1">
        <stop offset="0" stop-color="#18b7d0"/>
        <stop offset="0.5" stop-color="#d6c488"/>
        <stop offset="1" stop-color="#d6c488"/>
      </linearGradient>
      <radialGradient id="fire" cx="0.5" cy="0.55" r="0.6">
        <stop offset="0" stop-color="#ff9a2a"/>
        <stop offset="0.45" stop-color="#e0380e"/>
        <stop offset="1" stop-color="#3a0704"/>
      </radialGradient>
      <radialGradient id="badge" cx="0.3" cy="0.35" r="0.8">
        <stop offset="0" stop-color="#ffffff"/>
        <stop offset="0.5" stop-color="#f6e27a"/>
        <stop offset="1" stop-color="#f2c31c"/>
      </radialGradient>
      <clipPath id="backPanel"><rect x="598" y="33" width="582" height="811"/></clipPath>
      <clipPath id="frontPanel"><rect x="16" y="34" width="580" height="809"/></clipPath>
    </defs>

    <!-- front side -->
    <g class="front-side" clip-path="url(#frontPanel)">
      <rect x="16" y="34" width="580" height="809" fill="var(--ink)"/>
      <polygon points="258,34 400,34 596,230 596,340" fill="url(#stripeBlue)"/>
      <polygon points="330,34 390,34 596,240 596,300" fill="url(#stripeTeal)" opacity="0.8"/>
      <polygon points="300,34 330,34 596,300 596,330" fill="#0a5a9a" opacity="0.6"/>
      <polygon points="368,843 596,612 596,843" fill="url(#cornerBlue)"/>
    </g>

    <!-- back side -->
    <g class="back-side" clip-path="url(#backPanel)">
      <rect x="598" y="33" width="582" height="811" fill="var(--ink)"/>
      <polygon points="840,33 1010,33 1180,203 1180,330" fill="url(#stripeBlue)"/>
      <polygon points="900,33 950,33 1180,263 1180,313" fill="url(#stripeTeal)" opacity="0.8"/>
      <polygon points="598,250 730,380 598,380" fill="var(--gold-pale)"/>
      <polygon points="952,844 1180,612 1180,844" fill="url(#cornerGold)"/>

      <g role="img" aria-label="Powerlifting artwork: fiery horned strongman lifting a barbell">
        <polygon points="780,65 927,212 780,359 633,212" fill="url(#fire)" stroke="var(--ink)" stroke-width="6" stroke-linejoin="round"/>
      </g>
      <g role="img" aria-label="Martial arts artwork: fighter throwing a kick amid flames">
        <polygon points="958,157 1061,260 958,363 855,260" fill="url(#fire)" stroke="var(--ink)" stroke-width="6" stroke-linejoin="round"/>
      </g>
      <g role="img" aria-label="Boxing artwork: boxers in a lit arena">
        <polygon points="842,271 945,374 842,477 739,374" fill="url(#fire)" stroke="var(--ink)" stroke-width="6" stroke-linejoin="round"/>
      </g>
      <g role="img" aria-label="Bodybuilding artwork: armoured warrior with dumbbells">
        <polygon points="728,385 831,488 728,591 625,488" fill="url(#fire)" stroke="var(--ink)" stroke-width="6" stroke-linejoin="round"/>
      </g>
      <g role="img" aria-label="MMA artwork: champion with belt above a fighting cage in flames">
        <polygon points="1017,272 1231,486 1017,700 803,486" fill="url(#fire)" stroke="var(--ink)" stroke-width="6" stroke-linejoin="round"/>
      </g>

      <circle cx="776" cy="677" r="80" fill="none" stroke="var(--badge-yellow)" stroke-width="2.5" stroke-dasharray="8 6"/>
      <circle cx="776" cy="677" r="75" fill="url(#badge)"/>
    </g>
  </svg>

  <!-- front content -->
  <div class="shop-mark shop-mark--front">PUSH AND DUEL</div>
  <div class="shop-name">PUSH AND DUEL</div>

  <div class="product-card"></div>
  <h1 class="product-card__title">Product name for</h1>

  <div class="product-row" style="top:342px">
    <span class="product-row__sport">Powerlifting:</span>
    <span class="product-row__name">Torvik</span>
  </div>
  <div class="product-row" style="top:407px">
    <span class="product-row__sport">Boxing:</span>
    <span class="product-row__name">ZL Boxing</span>
  </div>
  <div class="product-row" style="top:472px">
    <span class="product-row__sport">Martial Arts:</span>
    <span class="product-row__name">Murelt</span>
  </div>
  <div class="product-row" style="top:537px">
    <span class="product-row__sport">MMA:</span>
    <span class="product-row__name">PitVolt</span>
  </div>
  <div class="product-row" style="top:602px">
    <span class="product-row__sport">Bodybuilding:</span>
    <span class="product-row__name">Bramfold</span>
  </div>

  <p class="brand-logos__label">BRAND LOGOS</p>
  <div class="brand-logos">
    <span class="brand-logos__slot"></span>
    <span class="brand-logos__slot"></span>
    <span class="brand-logos__slot"></span>
    <span class="brand-logos__slot"></span>
    <span class="brand-logos__slot"></span>
    <span class="brand-logos__slot"></span>
  </div>

  <!-- back content -->
  <div class="shop-mark shop-mark--back">PUSH AND DUEL</div>
  <div class="discount">
    <span class="discount__value">25%</span>
    <span class="discount__label">OFF</span>
  </div>
  <p class="website">www.pushandduel.example</p>

  <p class="caption caption--front">Front</p>
  <p class="caption caption--back">Back</p>
</main>
</body>
</html>
```